Professional Mothers Wordpress Site

*** To be clear, as a result of this contest I am looking for a fully functioning wordpress site to import into my wordpress site. Not just an image layout design.***

A Responsive Wordpress Blog Site for Professional Mothers

List of features desired:
1. Social media platform and commenting
2. Fully featured ecommerce store
3. Create and display fantastic-looking galleries of vimeo video content
4. Customised slideshows that are displayed in a content slider. Slides can be filled with text, images, video, social media stream feeds and syndicated content like Twitter feeds, YouTube, Pinterest, Flickr and more.
5. HTML5 and Flash compatible audio player that sits within the site. Works across both desktop and mobile devices
6. Admin panel
7. Google docs integrated email subscription, forms etc., email opt-in for newsletter
8. URL shortener
9. Enhanced image gallery
10. Interactive drag-and-drop pricing tables
11. Google Analytics, sitemaps
12. Rating system

List of pages on blogsite
1. Home page
2. About page
3. Resources page
4. Podcast archive page
5. Coaching page
6. Contact page

Here are some things I liked about the blogs I clicked through (and why I did or didn't like them)

Examples:
1) http://www.brindlecove.com/‎ - clean, professional feel
2) http://www.tessagrundvik.com/ - i like the simplicity of the email sign up and how it stands out without being obnoxious
3) http://clovertrailworks.com/ - i like the simplicity of the links to various pages at the top
4) http://www.velmarstudio.com/ - i like how the links are clear at the top and how they stay still even if the page moves (persistent headers)
5) http://www.hustlepanorama.com/ - i like how the podcast sessions are laid out on the front page
6) http://www.quorvane.com/ - this has a really nice 1st impression
7) http://dadwanderbook.com/ - this has a nice layout too but the logo is way too big and it takes too long to scroll down to the content
8) http://tiltbix.com/ - I like the moving content of this

Overall I'm going for something neat, clean and simple.

Target Market(s)

Working Mothers

Industry/Entity Type

Store

Requirements
Must have
• The social media links at the top of the page

```html
<!DOCTYPE html>
<html lang="en">
<head>
<meta charset="utf-8">
<title>Kindred Hours — Home</title>
<link href="https://fonts.googleapis.com/css2?family=Open+Sans:ital,wght@0,400;0,600;0,700;1,700&family=Roboto+Condensed:ital,wght@0,400;0,700;1,700&display=swap" rel="stylesheet">
<style>
:root{
  --magenta:#a8237f;
  --magenta-dark:#8a1b68;
  --band:#9b2787;
  --band-dark:#7e1d6d;
  --orange:#f29a1f;
  --ink:#333;
  --muted:#777;
  --line:#d8d8d8;
  --page:#f3f3f3;
  --card:#ffffff;
  --footer:#2b2b2b;
  --icon-grey:#9a9a9a;
  --blue:#3b5998;--red:#cb2027;--grey:#6f6f6f;--sky:#2fa6e0;--navy:#0e76a8;--coral:#dd4b39;
}
*{box-sizing:border-box;margin:0;padding:0}
html,body{width:1200px;height:3487px;overflow:hidden}
body{background:var(--page);font-family:"Open Sans",Arial,sans-serif;color:var(--ink);position:relative}
svg.icon{display:block;fill:#fff}

/* header */
.header{position:absolute;left:0;top:0;width:1200px;height:104px;background:#fff}
.brand{position:absolute;left:140px;top:22px;display:flex;align-items:center;gap:12px}
.brand-mark{width:26px;height:26px;border-radius:50%;background:var(--magenta)}
.brand-name{font-weight:700;font-size:30px;color:var(--magenta);letter-spacing:-.5px}
.social-top{position:absolute;right:139px;top:6px;display:flex;gap:8px}
.social-btn{width:30px;height:30px;border-radius:4px;background:var(--icon-grey);display:flex;align-items:center;justify-content:center}
.nav{position:absolute;left:508px;top:44px;display:flex}
.nav a{font-family:"Roboto Condensed",sans-serif;font-size:16px;color:#444;text-decoration:none;padding:14px 14px;text-transform:uppercase}
.nav a.active{background:var(--magenta);color:#fff;position:relative}
.nav a.active::after{content:"";position:absolute;left:50%;bottom:-8px;margin-left:-8px;border:8px solid transparent;border-top-color:var(--magenta);border-bottom:0}

/* hero */
.hero{position:absolute;left:140px;top:104px;width:921px;height:361px;background:linear-gradient(100deg,#c9b7a5 0%,#e7d3bf 40%,#bfd3dd 75%,#8fa9b8 100%)}
.hero-card{position:absolute;left:148px;top:122px;width:345px;height:343px;background:rgba(255,255,255,.94);padding:18px}
.hero-card h1{font-size:25px;line-height:30px;color:var(--magenta);font-weight:700}
.hero-card p{font-size:12px;line-height:17px;color:#555;margin-top:12px}
.share-row{display:flex;gap:6px;margin-top:14px}
.share-row .social-btn{width:24px;height:24px;border-radius:3px}
.share-count{display:flex;gap:6px;margin-top:10px}
.share-count span{width:52px;height:20px;border:1px solid #ccc;border-radius:3px;background:#f7f7f7;font-size:10px;line-height:18px;color:#555;text-align:center}

/* newsletter */
.newsletter{position:absolute;left:0;top:474px;width:1200px;height:72px;background:linear-gradient(var(--band),var(--band-dark))}
.newsletter .label{position:absolute;left:160px;top:22px;font-family:"Roboto Condensed",sans-serif;font-style:italic;font-weight:700;font-size:22px;color:#fff;text-transform:uppercase}
.field{position:absolute;top:18px;height:32px;background:#fff;border:1px solid #ccc;font-size:14px;color:#666;padding:6px 10px}
.get-it{position:absolute;left:880px;top:488px;width:68px;height:68px;border-radius:50%;background:var(--orange);border:3px solid #fff;color:#fff;font-family:"Roboto Condensed",sans-serif;font-style:italic;font-weight:700;font-size:19px;line-height:18px;text-align:center;padding-top:13px}

/* section headings */
.section-title{position:absolute;font-family:"Roboto Condensed",sans-serif;font-weight:700;font-size:21px;color:#333;text-transform:uppercase;border-bottom:1px solid var(--line);padding-bottom:8px}

/* video */
.video-main{position:absolute;left:140px;top:610px;width:623px;height:349px;background:linear-gradient(135deg,#9fc46b,#cfe0a8 50%,#e8e2d2)}
.video-bar{position:absolute;left:0;bottom:0;width:100%;height:34px;background:rgba(20,20,20,.85)}
.video-bar .play{position:absolute;left:14px;top:10px;border-left:14px solid #fff;border-top:8px solid transparent;border-bottom:8px solid transparent}
.video-bar .track{position:absolute;left:44px;right:110px;top:15px;height:4px;background:#666}
.video-bar .track i{display:block;width:30%;height:100%;background:#ddd}
.video-bar .hd{position:absolute;right:30px;top:9px;font-size:12px;font-weight:700;color:#fff}
.thumbs{position:absolute;left:770px;top:610px;width:291px;display:grid;grid-template-columns:143px 143px;gap:5px}
.thumb{height:84px}

/* posts */
.post{position:absolute;left:140px;width:645px;height:560px}
.date{position:absolute;left:10px;top:0;width:56px;height:56px;border-radius:50%;background:var(--magenta);color:#fff;text-align:center;font-family:"Roboto Condensed",sans-serif;line-height:1}
.date b{display:block;font-size:24px;padding-top:8px}
.date small{font-size:11px;text-transform:uppercase}
.post h2{position:absolute;left:78px;top:0;width:540px;font-size:24px;line-height:28px;font-weight:700;color:#222}
.post-media{position:absolute;left:10px;top:76px;width:518px;height:294px}
.post-meta{position:absolute;left:528px;top:76px;width:117px;height:294px;background:#fff;border:1px solid #e3e3e3;padding:10px 12px;font-size:12px}
.post-meta .comments{display:flex;align-items:center;gap:8px;font-weight:700;justify-content:flex-end}
.post-meta .comments svg{fill:#aaa}
.post-meta .rating{margin-top:16px;color:#666}
.stars{color:#ccc;font-size:15px;letter-spacing:1px}.stars em{color:var(--magenta);font-style:normal}
.mini-shares{position:absolute;left:12px;top:170px}
.mini-shares span{display:block;width:74px;height:18px;border:1px solid #ccc;background:#f7f7f7;border-radius:3px;margin-bottom:9px;font-size:10px;line-height:16px;padding-left:5px;color:#555}
.play-btn{position:absolute;left:50%;top:50%;width:60px;height:60px;margin:-30px 0 0 -30px;border-radius:50%;background:rgba(255,255,255,.85)}
.play-btn::after{content:"";position:absolute;left:23px;top:17px;border-left:20px solid #333;border-top:13px solid transparent;border-bottom:13px solid transparent}
.post p{position:absolute;left:10px;top:384px;width:625px;font-size:12px;line-height:18px;color:#555}
.btn{position:absolute;background:var(--magenta);color:#fff;font-family:"Roboto Condensed",sans-serif;font-weight:700;text-transform:uppercase;text-decoration:none}
.keep{left:10px;top:468px;width:185px;height:36px;font-size:17px;line-height:36px;padding-left:12px}
.keep::after{content:"›";position:absolute;right:12px;font-size:24px;top:-1px}

/* sidebar */
.product{position:absolute;left:831px;width:230px;height:220px}
.product-img{position:absolute;left:3px;top:0;width:134px;height:124px;border:4px solid #fff;box-shadow:0 1px 3px rgba(0,0,0,.2)}
.product-desc{position:absolute;left:0;top:134px;width:160px;font-size:11px;line-height:15px;color:#555}
.price{position:absolute;left:0;top:176px;font-size:11px;color:#777}
.price b{display:block;font-size:16px;color:#333}
.buy{left:132px;top:180px;width:98px;height:32px;font-size:15px;line-height:32px;text-align:center}
.popular{position:absolute;left:831px;top:1836px;width:230px;list-style:none}
.popular li{font-size:12px;line-height:16px;color:var(--magenta);border-bottom:1px solid #e5e5e5;padding:6px 0 8px}
.sb-rule{position:absolute;left:831px;top:2178px;width:230px;height:3px;background:#999}
.feed{position:absolute;left:831px;width:230px;height:278px;background:#fff;border:1px solid #e3e3e3}
.feed-img{height:132px;margin:8px}
.feed p{font-size:11px;line-height:15px;color:#555;padding:2px 12px}
.feed-bar{position:absolute;left:0;bottom:0;width:100%;height:54px;color:#fff;padding:8px 10px;font-size:12px;font-weight:700}
.feed-bar small{display:block;font-weight:400;font-size:10px;opacity:.85}
.feed-bar .social-btn{position:absolute;right:10px;top:11px;width:32px;height:32px;background:rgba(255,255,255,.25)}

/* footer */
.footer{position:absolute;left:0;top:3420px;width:1200px;height:67px;background:var(--footer);color:#fff;text-align:center}
.footer nav{padding-top:13px;font-family:"Roboto Condensed",sans-serif;font-size:14px;text-transform:uppercase}
.footer nav a{color:#fff;text-decoration:none;margin:0 16px}
.footer .legal{font-size:11px;margin-top:8px;color:#ddd;text-transform:uppercase}
</style>
</head>
<body>

<svg width="0" height="0" style="position:absolute" aria-hidden="true">
  <defs>
    <symbol id="i-chat" viewBox="0 0 16 16"><path d="M2 2h12a1 1 0 0 1 1 1v7a1 1 0 0 1-1 1H7l-4 3v-3H2a1 1 0 0 1-1-1V3a1 1 0 0 1 1-1z"/></symbol>
    <symbol id="i-share" viewBox="0 0 16 16"><circle cx="12" cy="3.5" r="2.3"/><circle cx="4" cy="8" r="2.3"/><circle cx="12" cy="12.5" r="2.3"/><path d="M4 8l8-4.5M4 8l8 4.5" stroke="#fff" stroke-width="1.4" fill="none"/></symbol>
    <symbol id="i-mail" viewBox="0 0 16 16"><path d="M1 3h14v10H1z"/><path d="M1.5 3.5L8 9l6.5-5.5" stroke="#9a9a9a" stroke-width="1.3" fill="none"/></symbol>
    <symbol id="i-plus" viewBox="0 0 16 16"><path d="M6.5 2h3v4.5H14v3H9.5V14h-3V9.5H2v-3h4.5z"/></symbol>
    <symbol id="i-heart" viewBox="0 0 16 16"><path d="M8 14L2.2 8.4A3.4 3.4 0 0 1 8 4a3.4 3.4 0 0 1 5.8 4.4z"/></symbol>
    <symbol id="i-link" viewBox="0 0 16 16"><path d="M6.5 9.5l3-3" stroke="#fff" stroke-width="1.8"/><path d="M7 4.5l1.5-1.5a2.8 2.8 0 0 1 4 4L11 8.5M9 11.5L7.5 13a2.8 2.8 0 0 1-4-4L5 7.5" stroke="#fff" stroke-width="1.8" fill="none"/></symbol>
  </defs>
</svg>

<header class="header">
  <div class="brand"><span class="brand-mark"></span><span class="brand-name">Kindred Hours</span></div>
  <div class="social-top" aria-label="Follow us">
    <a class="social-btn" aria-label="Community chat"><svg class="icon" width="16" height="16"><use href="#i-chat"/></svg></a>
    <a class="social-btn" aria-label="Share"><svg class="icon" width="16" height="16"><use href="#i-share"/></svg></a>
    <a class="social-btn" aria-label="Email"><svg class="icon" width="16" height="16"><use href="#i-mail"/></svg></a>
    <a class="social-btn" aria-label="Follow"><svg class="icon" width="16" height="16"><use href="#i-plus"/></svg></a>
    <a class="social-btn" aria-label="Favourites"><svg class="icon" width="16" height="16"><use href="#i-heart"/></svg></a>
    <a class="social-btn" aria-label="Copy link"><svg class="icon" width="16" height="16"><use href="#i-link"/></svg></a>
  </div>
  <nav class="nav">
    <a class="active" href="#">Home</a><a href="#">About</a><a href="#">Resources</a><a href="#">Podcast Archive</a><a href="#">Coaching</a><a href="#">Contact</a>
  </nav>
</header>

<section class="hero" role="img" aria-label="Slideshow photo of a mother hugging her smiling daughter"></section>
<div class="hero-card">
  <h1>Lorem ipsum dolor sit amet, consectetur adipisicing elit.</h1>
  <p>Sed ut perspiciatis unde omnis iste natus error sit voluptatem accusantium doloremque laudantium, totam rem aperiam, eaque ipsa quae ab illo inventore veritatis et quasi architecto beatae vitae dicta sunt explicabo. Nemo enim ipsam voluptatem quia voluptas sit aspernatur.</p>
  <div class="share-row">
    <span class="social-btn" style="background:var(--blue)"><svg class="icon" width="14" height="14"><use href="#i-chat"/></svg></span>
    <span class="social-btn" style="background:var(--sky)"><svg class="icon" width="14" height="14"><use href="#i-share"/></svg></span>
    <span class="social-btn" style="background:var(--navy)"><svg class="icon" width="14" height="14"><use href="#i-link"/></svg></span>
    <span class="social-btn" style="background:var(--coral)"><svg class="icon" width="14" height="14"><use href="#i-plus"/></svg></span>
    <span class="social-btn" style="background:var(--orange)"><svg class="icon" width="14" height="14"><use href="#i-mail"/></svg></span>
    <span class="social-btn" style="background:var(--red)"><svg class="icon" width="14" height="14"><use href="#i-heart"/></svg></span>
  </div>
  <div class="share-count"><span>Like 12</span><span>Share 8</span><span>Post 5</span><span>Save 3</span></div>
</div>

<section class="newsletter">
  <div class="label">Signup for Newsletter</div>
  <div class="field" style="left:540px;width:118px">First Name</div>
  <div class="field" style="left:668px;width:198px">E-Mail</div>
</section>
<div class="get-it">Get<br>it!</div>

<h3 class="section-title" style="left:140px;top:556px;width:921px">Video Galleries</h3>
<div class="video-main" role="img" aria-label="Featured video still of a mother lifting her baby on the grass">
  <div class="video-bar"><span class="play"></span><span class="track"><i></i></span><span class="hd">HD</span></div>
</div>
<div class="thumbs">
  <div class="thumb" role="img" aria-label="Video thumbnail" style="background:#c9a890"></div>
  <div class="thumb" role="img" aria-label="Video thumbnail" style="background:#d9c4b3"></div>
  <div class="thumb" role="img" aria-label="Video thumbnail" style="background:#b9a08a"></div>
  <div class="thumb" role="img" aria-label="Video thumbnail" style="background:#e0cdbd"></div>
  <div class="thumb" role="img" aria-label="Video thumbnail" style="background:#cdb6a0"></div>
  <div class="thumb" role="img" aria-label="Video thumbnail" style="background:#a9bca0"></div>
  <div class="thumb" role="img" aria-label="Video thumbnail" style="background:#d6b9a4"></div>
  <div class="thumb" role="img" aria-label="Video thumbnail" style="background:#8f7d86"></div>
</div>

<h3 class="section-title" style="left:140px;top:992px;width:645px">Blogs</h3>
<h3 class="section-title" style="left:831px;top:992px;width:230px">Ecommerce Store</h3>

<article class="post" style="top:1040px">
  <div class="date"><b>10</b><small>Jun</small></div>
  <h2>Lorem ipsum dolor sit amet, consectetur adipisicing elit.</h2>
  <div class="post-media" role="img" aria-label="Blog photo of a mother and child in warm sunlight" style="background:linear-gradient(135deg,#d9a55a,#f2d38c 55%,#b8894f)"></div>
  <div class="post-meta"><div class="comments"><svg width="14" height="14"><use href="#i-chat"/></svg>15</div><div class="rating">Rating<div class="stars"><em>★★★</em>★★</div></div>
    <div class="mini-shares"><span>Like 340</span><span>Share 308</span><span>Post 17</span><span>Save 0</span></div></div>
  <p>Sed ut perspiciatis unde omnis iste natus error sit voluptatem accusantium doloremque laudantium, totam rem aperiam, eaque ipsa quae ab illo inventore veritatis et quasi architecto beatae vitae dicta sunt explicabo. Nemo enim ipsam voluptatem quia voluptas sit aspernatur aut odit aut fugit, sed quia consequuntur magni dolores eos qui ratione voluptatem sequi nesciunt.</p>
  <a class="btn keep" href="#">Keep Reading</a>
</article>

<article class="post" style="top:1628px">
  <div class="date"><b>10</b><small>Jun</small></div>
  <h2>Lorem ipsum dolor sit amet, consectetur adipisicing elit.</h2>
  <div class="post-media" role="img" aria-label="Video still of a mother and daughter smiling together" style="background:linear-gradient(135deg,#d8cfc4,#efe6da 50%,#c6b6a6)"><span class="play-btn"></span></div>
  <div class="post-meta"><div class="comments"><svg width="14" height="14"><use href="#i-chat"/></svg>15</div><div class="rating">Rating<div class="stars"><em>★★★</em>★★</div></div>
    <div class="mini-shares"><span>Like 340</span><span>Share 308</span><span>Post 17</span><span>Save 0</span></div></div>
  <p>Sed ut perspiciatis unde omnis iste natus error sit voluptatem accusantium doloremque laudantium, totam rem aperiam, eaque ipsa quae ab illo inventore veritatis et quasi architecto beatae vitae dicta sunt explicabo. Nemo enim ipsam voluptatem quia voluptas sit aspernatur aut odit aut fugit, sed quia consequuntur magni dolores eos qui ratione voluptatem sequi nesciunt.</p>
  <a class="btn keep" href="#">Keep Reading</a>
</article>

<article class="post" style="top:2216px">
  <div class="date"><b>10</b><small>Jun</small></div>
  <h2>Lorem ipsum dolor sit amet, consectetur adipisicing elit.</h2>
  <div class="post-media" role="img" aria-label="Video still of a mother at a laptop beside her son with a tablet" style="background:linear-gradient(135deg,#e9e9ec,#d4d6dc 55%,#b9bdc6)"><span class="play-btn"></span></div>
  <div class="post-meta"><div class="comments"><svg width="14" height="14"><use href="#i-chat"/></svg>15</div><div class="rating">Rating<div class="stars"><em>★★★</em>★★</div></div>
    <div class="mini-shares"><span>Like 340</span><span>Share 308</span><span>Post 17</span><span>Save 0</span></div></div>
  <p>Sed ut perspiciatis unde omnis iste natus error sit voluptatem accusantium doloremque laudantium, totam rem aperiam, eaque ipsa quae ab illo inventore veritatis et quasi architecto beatae vitae dicta sunt explicabo. Nemo enim ipsam voluptatem quia voluptas sit aspernatur aut odit aut fugit, sed quia consequuntur magni dolores eos qui ratione voluptatem sequi nesciunt.</p>
  <a class="btn keep" href="#">Keep Reading</a>
</article>

<article class="post" style="top:2804px">
  <div class="date"><b>10</b><small>Jun</small></div>
  <h2>Lorem ipsum dolor sit amet, consectetur adipisicing elit.</h2>
  <div class="post-media" role="img" aria-label="Blog photo of a mother lifting her baby on the grass" style="background:linear-gradient(135deg,#9fc46b,#d6e4ae 50%,#e6dccb)"></div>
  <div class="post-meta"><div class="comments"><svg width="14" height="14"><use href="#i-chat"/></svg>15</div><div class="rating">Rating<div class="stars"><em>★★★</em>★★</div></div>
    <div class="mini-shares"><span>Like 340</span><span>Share 308</span><span>Post 17</span><span>Save 0</span></div></div>
  <p>Sed ut perspiciatis unde omnis iste natus error sit voluptatem accusantium doloremque laudantium, totam rem aperiam, eaque ipsa quae ab illo inventore veritatis et quasi architecto beatae vitae dicta sunt explicabo. Nemo enim ipsam voluptatem quia voluptas sit aspernatur aut odit aut fugit, sed quia consequuntur magni dolores eos qui ratione voluptatem sequi nesciunt.</p>
  <a class="btn keep" href="#">Keep Reading</a>
</article>

<div class="product" style="top:1048px">
  <div class="product-img" role="img" aria-label="Product photo of a mother and son" style="background:#b9c7cf"></div>
  <div class="product-desc">Lorem ipsum dolor sit amet, consectetur adipisicing elit</div>
  <div class="price">Price<b>$50.00</b></div><a class="btn buy" href="#">Buy Now</a>
</div>
<div class="product" style="top:1292px">
  <div class="product-img" role="img" aria-label="Product photo of a mother and baby" style="background:#ded6d0"></div>
  <div class="product-desc">Lorem ipsum dolor sit amet, consectetur adipisicing elit</div>
  <div class="price">Price<b>$50.00</b></div><a class="btn buy" href="#">Buy Now</a>
</div>
<div class="product" style="top:1536px">
  <div class="product-img" role="img" aria-label="Product photo of a mother kissing her child" style="background:#d4b3a4"></div>
  <div class="product-desc">Lorem ipsum dolor sit amet, consectetur adipisicing elit</div>
  <div class="price">Price<b>$50.00</b></div><a class="btn buy" href="#">Buy Now</a>
</div>

<h3 class="section-title" style="left:831px;top:1790px;width:230px;border:0">Most Popular</h3>
<ul class="popular">
  <li>Proin id ligula id mauris luctus aliquam nec a libero</li>
  <li>Morbi aliquet odio at libero rutrum sagittis</li>
  <li>Nulla sed mi dapibus lacus bibendum vulputate</li>
  <li>Phasellus sed lacus a felis venenatis eleifend</li>
  <li>Morbi aliquet odio at libero rutrum sagittis</li>
  <li>Nulla sed mi dapibus lacus bibendum vulputate</li>
  <li>Phasellus sed lacus a felis venenatis eleifend</li>
</ul>
<div class="sb-rule"></div>

<div class="feed" style="top:2200px">
  <div class="feed-img" role="img" aria-label="Feed photo of a mother and son" style="background:#c8d3dc"></div>
  <p>Sed ut perspiciatis unde omnis iste natus error sit voluptatem accusantium doloremque laudantium, totam rem aperiam.</p>
  <div class="feed-bar" style="background:var(--blue)">Lorem ipsum dolor<small>1 days ago</small><span class="social-btn"><svg class="icon" width="16" height="16"><use href="#i-chat"/></svg></span></div>
</div>
<div class="feed" style="top:2492px">
  <div class="feed-img" role="img" aria-label="Feed photo of a mother and baby" style="background:#e0d7d0"></div>
  <p>Sed ut perspiciatis unde omnis iste natus error sit voluptatem accusantium doloremque laudantium, totam rem aperiam.</p>
  <div class="feed-bar" style="background:var(--red)">Lorem ipsum dolor<small>1 days ago</small><span class="social-btn"><svg class="icon" width="16" height="16"><use href="#i-heart"/></svg></span></div>
</div>
<div class="feed" style="top:2784px">
  <div class="feed-img" role="img" aria-label="Feed photo of a mother working beside her son" style="background:#dadde2"></div>
  <p>Sed ut perspiciatis unde omnis iste natus error sit voluptatem accusantium doloremque laudantium, totam rem aperiam.</p>
  <div class="feed-bar" style="background:var(--grey)">Lorem ipsum dolor<small>1 days ago</small><span class="social-btn"><svg class="icon" width="16" height="16"><use href="#i-link"/></svg></span></div>
</div>
<div class="feed" style="top:3076px">
  <div class="feed-img" role="img" aria-label="Feed photo of a mother and baby outdoors" style="background:#b9cf95"></div>
  <p>Sed ut perspiciatis unde omnis iste natus error sit voluptatem accusantium doloremque laudantium, totam rem aperiam.</p>
  <div class="feed-bar" style="background:var(--sky)">Lorem ipsum dolor<small>1 days ago</small><span class="social-btn"><svg class="icon" width="16" height="16"><use href="#i-share"/></svg></span></div>
</div>

<footer class="footer">
  <nav><a href="#">Home</a><a href="#">About</a><a href="#">Resources</a><a href="#">Podcast Archive</a><a href="#">Coaching</a><a href="#">Contact</a></nav>
  <div class="legal">Privacy Policy | © 2013 Kindred Hours | Terms Policy | Disclaimer</div>
</footer>

</body>
</html>
```